Bed & Breakfast Wordpress Theme - Design Only

We are looking for a Wordpress theme for an award winning UK Bed & Breakfast (Guesthouse) www.fernbrookhouse.co.uk
You will see that the current site is basic and dated, we need a new site that showcases the very high standard of rooms on offer and is geared towards both mobile and desktop browsing.
We would like the colours that have been used in the rooms and building (as seen on the current website) to feature in the design.
We particularly like the look of this accommodation provider website: http://www.wrenmeadowbarns.co.uk
Selected website images can be downloaded here, feel free to use more from the existing website too:
https://www.filevaultly.com/s/qa7mr41xt8zv2kp/website%20images.zip
Target Market(s)
The accommodation is upmarket and the design needs to subtly communicate this.
The accommodation attracts a varied mix of ages so needs to be up scale without being overly modern.
Industry/Entity Type
Accommodation
Requirements
Must have
- As the accommodation does not have a logo we need a basic typographic logo incorporated into the design.
Colours of the building and rooms must be integrated into the design in some way.
A bold homepage that allows images of the rooms on offer and key information to be visibale above the fold. The goal of the homepage is for someone to then click Rooms or Prices so calls to action may help here.
Separate designs for a sidebar and full width version of sub pages.
An area that shows off the awards won by the company on all pages and space for testimonials.
The site must enable an easy transition from - homepage - to rooms - to prices with possible call to action buttons in the top right corner on these pages
The site needs to have a Homepage layout, a general sub page layout, and a 'Rooms' page layout which will showcase all rooms available possibly in a grid layout.
Nice to have
- Please use some of the images available currently on the website in your mockup, particularly of the building and rooms.
Should not have
- No need for any type of booking fields or engine as the booking system will be embedded on a full width page.

```html
<!DOCTYPE html>
<html lang="en">
<head>
<meta charset="utf-8">
<title>Fernbrook House</title>
<link href="https://fonts.googleapis.com/css2?family=Roboto+Slab:wght@300;400&family=Ubuntu:wght@300;400;500&display=swap" rel="stylesheet">
<style>
:root{
  --brown:#7a6a5d;--dark:#4a3f36;--ink:#333;--body:#666;--muted:#888;
  --line:#e2e2e2;--green-bg:#dfe8c8;--green:#6a8a38;--quote:#dcd8d2;--foot:#ebebeb;
}
*{margin:0;padding:0;box-sizing:border-box}
html,body{width:917px;height:1200px;overflow:hidden;background:#fff}
body{position:relative;font-family:Ubuntu,sans-serif;color:var(--body)}
.abs{position:absolute}
.topbar{left:0;top:0;width:917px;height:30px;background:var(--brown);color:#e8e0d8;font-size:8px;line-height:30px}
.topbar b{font-weight:400;color:#fff}
.header{left:0;top:30px;width:917px;height:56px;background:#fff;border-bottom:1px solid #ddd}
.logo{font-family:'Roboto Slab',serif;font-weight:300;color:#3a3a3a;font-size:18px;letter-spacing:.2px}
.nav{left:395px;top:22px;display:flex;gap:27px;font-family:'Roboto Slab',serif;font-weight:300;font-size:9.5px;color:#555}
.photo{box-shadow:inset 0 0 0 1px rgba(0,0,0,.06)}
.hero{left:0;top:86px;width:917px;height:284px;
  background:
    radial-gradient(ellipse 120px 90px at 30% 38%,rgba(255,236,190,.85),transparent 70%),
    radial-gradient(ellipse 110px 80px at 57% 38%,rgba(255,236,190,.8),transparent 70%),
    radial-gradient(ellipse 230px 90px at 43% 82%,rgba(250,248,244,.95),transparent 75%),
    radial-gradient(ellipse 90px 160px at 52% 45%,rgba(150,115,75,.55),transparent 70%),
    radial-gradient(ellipse 140px 140px at 10% 70%,rgba(70,55,40,.7),transparent 70%),
    linear-gradient(90deg,#8a7660 0%,#c8ab84 25%,#e2cfb2 50%,#d7c3a6 72%,#efe8dd 100%)}
.hero-arrow{width:40px;height:42px;top:196px;background:rgba(60,55,50,.6)}
.caption{left:0;top:308px;width:917px;height:62px;background:rgba(50,44,40,.72)}
.caption h1{position:absolute;left:152px;top:10px;font-family:'Roboto Slab',serif;font-weight:400;font-size:26px;color:#fff}
.caption p{position:absolute;left:307px;top:13px;width:300px;font-size:11px;line-height:18px;color:#fff;font-weight:300}
.btn{left:623px;top:16px;width:133px;height:30px;background:var(--green-bg);border:1px solid #c6d4a4;color:var(--green);font-size:7.5px;font-weight:500;line-height:28px}
.btn span.t{position:absolute;left:41px}
.h2{font-family:'Roboto Slab',serif;font-weight:300;font-size:12px;color:#333;background:#fff;padding-right:6px}
.rule{height:4px;border-top:1px solid var(--line);border-bottom:1px solid var(--line)}
.thumb{top:421px;width:118px;height:90px}
.sarrow{width:20px;height:19px;top:457px;background:#ddd}
.txt{font-size:7.5px;line-height:13px;color:var(--body)}
.list{left:153px;top:790px;list-style:none;font-size:7.5px;color:#666}
.list li{height:22.4px;display:flex;align-items:center;gap:9px}
.dot{width:12px;height:12px;border-radius:50%;background:#9b8a7c;display:inline-block;position:relative}
.dot:after{content:"";position:absolute;left:3px;top:4px;width:3px;height:3px;border-right:1.5px solid #fff;border-top:1.5px solid #fff;transform:rotate(45deg)}
.quote{left:468px;top:796px;width:296px;height:98px;background:var(--quote);padding:15px 16px;font-size:7.3px;line-height:13px;font-style:italic;color:#777}
.footer{left:0;top:966px;width:917px;height:194px;background:var(--foot)}
.footer:before{content:"";position:absolute;left:130px;top:0;width:657px;height:6px;background:radial-gradient(ellipse at 50% 0,rgba(0,0,0,.12),transparent 70%)}
.fh{font-size:8.5px;color:#333;text-transform:uppercase}
.fs{font-size:6px;color:#888}
.fp{font-size:8.5px;line-height:13px;color:#777}
.bottom{left:0;top:1160px;width:917px;height:40px;background:var(--dark);color:#c8bdb2;font-size:7.5px;line-height:40px}
.social{width:11px;height:11px;border-radius:2px;background:#777;display:inline-block;margin-right:12px}
</style>
</head>
<body>

<div class="abs topbar">
  <span class="abs" style="left:152px">ADDRESS: <b>Fernbrook House, Mill Lane, Ashcombe, Dorset DT9 4QR</b></span>
  <span class="abs" style="left:510px">EMAIL: <b>enquiries@fernbrookhouse.co.uk</b></span>
  <span class="abs" style="left:684px">CALL US: <b>1-500-555-0142</b></span>
</div>

<div class="abs header">
  <div class="abs logo" style="left:152px;top:15px">Fernbrook House</div>
  <nav class="abs nav"><span>Home</span><span>Rooms</span><span>Prices</span><span>Picture Gallery</span><span>Information</span><span>Contact</span></nav>
</div>

<div class="abs hero photo" role="img" aria-label="Photograph of a guest bedroom with a king size driftwood bed, lamps and wicker chairs"></div>
<div class="abs hero-arrow" style="left:0"><svg width="40" height="42"><path d="M23 14 L16 21 L23 28" stroke="#fff" stroke-width="2" fill="none"/></svg></div>
<div class="abs hero-arrow" style="left:877px"><svg width="40" height="42"><path d="M17 14 L24 21 L17 28" stroke="#fff" stroke-width="2" fill="none"/></svg></div>
<div class="abs caption">
  <h1>Larchwood</h1>
  <p>First floor, bath with shower over. Completely refurbished with king size drift wood bed April 2012</p>
  <div class="abs btn">
    <svg class="abs" style="left:13px;top:9px" width="10" height="10"><rect x="1" y="2" width="8" height="7" fill="none" stroke="#6a8a38"/><line x1="1" y1="4" x2="9" y2="4" stroke="#6a8a38"/></svg>
    <span style="position:absolute;left:31px;top:3px;bottom:3px;width:1px;background:#c6d4a4"></span>
    <span class="t">CHECK AVAILABILITY</span>
  </div>
</div>

<div class="abs rule" style="left:152px;top:393px;width:616px"></div>
<div class="abs h2" style="left:152px;top:386px">Featured Rooms</div>
<div class="abs sarrow" style="left:150px"><svg width="20" height="19"><path d="M11 6 L8 9.5 L11 13" stroke="#fff" stroke-width="1.5" fill="none"/></svg></div>
<div class="abs sarrow" style="left:746px"><svg width="20" height="19"><path d="M9 6 L12 9.5 L9 13" stroke="#fff" stroke-width="1.5" fill="none"/></svg></div>
<div class="abs thumb photo" style="left:190px;background:radial-gradient(ellipse 50px 30px at 70% 75%,rgba(120,80,90,.55),transparent 70%),radial-gradient(ellipse 60px 40px at 30% 30%,#fbfaf7,transparent 70%),linear-gradient(135deg,#efece6,#c8bdb0 70%,#a8998a)" role="img" aria-label="Bright attic bedroom with four poster bed"></div>
<div class="abs thumb photo" style="left:329px;background:radial-gradient(ellipse 60px 40px at 50% 30%,#7d7868,transparent 75%),linear-gradient(180deg,#4d4a44,#5e5a4e 60%,#6e6a5c)" role="img" aria-label="Room photograph with hover overlay">
  <div class="abs" style="left:49px;top:20px;width:20px;height:20px;border-radius:50%;background:#333"><svg width="20" height="20"><circle cx="9" cy="9" r="3.5" stroke="#fff" stroke-width="1.5" fill="none"/><line x1="11.5" y1="11.5" x2="14" y2="14" stroke="#fff" stroke-width="1.5"/></svg></div>
  <div class="abs" style="left:0;top:45px;width:118px;text-align:center;color:#fff;font-family:'Roboto Slab',serif;font-size:10px">Room Name</div>
  <div class="abs" style="left:0;top:60px;width:118px;text-align:center;color:#eee;font-size:6.5px;line-height:9px">Short description about<br>the room</div>
</div>
<div class="abs thumb photo" style="left:469px;background:radial-gradient(ellipse 50px 25px at 40% 78%,#f3efe8,transparent 75%),radial-gradient(ellipse 25px 25px at 82% 55%,rgba(255,214,130,.9),transparent 70%),linear-gradient(90deg,#6b4a2e,#b08860 40%,#8a7060 75%,#5a4030)" role="img" aria-label="Warm lit bedroom with wooden panelling"></div>
<div class="abs thumb photo" style="left:609px;background:radial-gradient(ellipse 25px 25px at 78% 45%,rgba(90,70,90,.7),transparent 75%),radial-gradient(ellipse 40px 12px at 50% 95%,rgba(200,120,110,.6),transparent 75%),linear-gradient(90deg,#2f3338 0%,#3a3e44 30%,#cfc8bc 50%,#b7ad9f 100%)" role="img" aria-label="Wood burning stove beside a wicker armchair"></div>

<div class="abs h2" style="left:152px;top:563px">Welcome to Fernbrook House - A Small and friendly hotel.</div>
<div class="abs photo" style="left:154px;top:592px;width:118px;height:134px;background:radial-gradient(ellipse 60px 70px at 45% 45%,#efeae1,transparent 75%),linear-gradient(135deg,#e3ddd2,#c9bfb0)" role="img" aria-label="Hand lettered welcome sign on a cream wall"></div>
<div class="abs txt" style="left:293px;top:592px;width:280px"><b style="font-weight:500;color:#555">Award-Winning</b>, Eco Chic, Environmentally-Responsible, New Forest Accom­modation offering 24 hour front desk, daily housekeeping, private bathroom for every room.<br><br>Eu tortor euismodolo. Vestibulum ant psu meop primis inicibu orci luctus ed ultrices et posuere cubil. Cura sed quis nibhut odiocinialor matis ed iaculis ante sed vel laciniate. Eu tortor euismodolo. Vestibulum ant psu meop primis inicibu orci luctus ed ultrices et posuere cubil. Cura sed quis nibhut odiocinialor matis ed iaculis ante sed vel laciniate.</div>

<div class="abs h2" style="left:608px;top:563px">Latest From The Blog</div>
<div class="abs photo" style="left:606px;top:596px;width:160px;height:58px;background:radial-gradient(ellipse 20px 25px at 92% 60%,rgba(90,120,60,.8),transparent 75%),radial-gradient(ellipse 25px 12px at 20% 85%,rgba(40,40,40,.7),transparent 75%),linear-gradient(180deg,#b7c6d6 0%,#dfe2e2 25%,#f2f1ec 45%,#e6e4dc 75%,#8b8f7a 100%)" role="img" aria-label="White guesthouse exterior with a yellow door"></div>
<div class="abs" style="left:606px;top:666px;font-family:'Roboto Slab',serif;font-size:8.5px;color:#333">Rent an Electric Runabout for just £20 per half hour.</div>
<div class="abs" style="left:606px;top:681px;font-size:6.5px;color:#444">Jan 03 2014 &nbsp;|&nbsp; 10 Comments</div>
<div class="abs txt" style="left:606px;top:699px;width:165px">Lid est laborum dolo rumes fugats esi untras. Etharums ser quidem rerums facilis</div>

<div class="abs rule" style="left:153px;top:766px;width:299px"></div>
<div class="abs h2" style="left:153px;top:759px">Why Choose Us?</div>
<ul class="abs list">
  <li><i class="dot"></i>Cras rutrum leo at odio volutpat id blandit fugiats ipsum ornare.</li>
  <li><i class="dot"></i>Donec fermentum porttitor nunc, sit amet gravida est porttitor vel.</li>
  <li><i class="dot"></i>Maecenas quis nisi in uctus adipiscing sed vehicvula tellus amet dolore.</li>
  <li><i class="dot"></i>Aenean faucibus sapien a odio varius aliquet voluptas sadips..</li>
  <li><i class="dot"></i>Suspendisse venenatis euismod ve vestibulum volutpat nibh imperdiets.</li>
  <li><i class="dot"></i>Quisque non leo molestie augue imperdiet sollicitudin eu nec urna.</li>
</ul>

<div class="abs rule" style="left:466px;top:766px;width:299px"></div>
<div class="abs h2" style="left:466px;top:759px">What Client’s Say</div>
<div class="abs quote">"Neque porro quisquam est, qui dolorem ipsum quia dolor sit amet, consec tetur, adipisci velit, sed quia non numquam eius modi tempora incidunt utis labore et dolore magnam aliquam quaerat voluptatem. Ut enim ad minimas veniam, quis nostrum exercitationem ullam corporis suscipit laboriosam, nisi ut aliquid ex ea commodi consequatur slores amet untras vel illum qui."</div>
<svg class="abs" style="left:494px;top:894px" width="14" height="10"><path d="M0 0 L14 0 L0 10 Z" fill="#dcd8d2"/></svg>
<div class="abs" style="left:469px;top:907px;font-size:7.5px;color:#555"><b style="font-weight:500;color:#333">Ellen Marsh,</b> Marsh &amp; Co.</div>

<div class="abs footer">
  <div class="abs logo" style="left:151px;top:26px">Fernbrook House</div>
  <div class="abs" style="left:152px;top:53px;width:145px;font-size:7px;line-height:13px;color:#777">Award-Winning, Eco Chic, Environmentally-Responsible, New Forest Accommodation offering 24 hour front desk, daily housekeeping, private</div>
  <div class="abs fh" style="left:152px;top:137px">Get Social</div>
  <div class="abs" style="left:152px;top:158px"><i class="social"></i><i class="social"></i><i class="social"></i><i class="social"></i><i class="social"></i></div>

  <div class="abs fh" style="left:309px;top:29px">Recent Posts</div>
  <div class="abs fs" style="left:309px;top:53px">DEC 15, 2012 &nbsp;| &nbsp;BY ADMIN</div>
  <div class="abs fp" style="left:309px;top:63px">Morbi a libero eget erat auctor<br>Sus vitae id tortor suspendisse.<br>Vestibulum eu ligula lorem ...</div>
  <div class="abs fs" style="left:309px;top:124px">DEC 15, 2012 &nbsp;| &nbsp;BY ADMIN</div>
  <div class="abs fp" style="left:309px;top:134px">Morbi a libero eget erat auctor<br>Sus vitae id tortor suspendisse.<br>Vestibulum eu ligula lorem ...</div>

  <div class="abs fh" style="left:466px;top:29px">Contacts</div>
  <div class="abs fp" style="left:466px;top:51px">Harbourline Ltd.<br>PO Box 4402<br>Quayside Row, Ashcombe<br>Dorset DT9 4QR UK</div>
  <div class="abs fp" style="left:466px;top:116px">Phone: (415) 555-0190<br>Fax: (415) 555-0191</div>
  <div class="abs fp" style="left:466px;top:156px">support@fernbrookhouse.co.uk</div>

  <div class="abs fh" style="left:624px;top:29px">Awards</div>
  <div class="abs" style="left:626px;top:50px;width:34px;height:34px;border-radius:50%;border:3px solid #d28a3a;background:#f3d9b4"></div>
  <div class="abs" style="left:624px;top:88px;width:38px;height:20px;background:#efe3cf;border-top:2px solid #d28a3a;border-bottom:2px solid #d28a3a"></div>
  <div class="abs" style="left:682px;top:57px;width:46px;height:46px;background:radial-gradient(circle at 40% 35%,#3c4d85,#1f2b55);border-radius:50%;box-shadow:0 1px 3px rgba(0,0,0,.3)"></div>
  <div class="abs" style="left:730px;top:126px;width:20px;height:20px;background:#a8263a;transform:rotate(45deg)"></div>
  <div class="abs" style="left:620px;top:150px;width:130px;height:3px;background:#6b5a3a"></div>
  <div class="abs" style="left:620px;top:157px;width:130px;height:16px;background:#ddd4c4;border-radius:2px"></div>
</div>

<div class="abs bottom">
  <span class="abs" style="left:152px">© 2014 Fernbrook House. All Rights Reserved</span>
  <span class="abs" style="right:156px">Home | Rooms | Tariffs | Activities | Eating &amp; Drinking | Travel | Links | Sitemap</span>
</div>

</body>
</html>
```